SPÄTER FREI!
Zielgruppe
Mein Ebook 'SPÄTER FREI!' soll den Untertitel 'Wie du Depressionen, Süchte und Einsamkeit überwindest und dein Leben veränderst' haben. Genau darum geht es und das soll das auch Cover vermitteln. Der Autor des Buches heißt Olaf Brenner.

```html
<!DOCTYPE html>
<html lang="de">
<head>
<meta charset="utf-8">
<title>SPÄTER FREI! – Olaf Brenner</title>
<link rel="stylesheet" href="https://fonts.googleapis.com/css2?family=Cabin+Sketch:wght@700&family=Fredoka:wght@600&display=swap">
<style>
  :root {
    --paper: #fbfbfc;
    --blue: #0a6fbd;
    --cyan: #0aa3e0;
    --red: #d3211f;
    --green: #3aa535;
    --pink: #e4127f;
    --shirt: #34363c;
    --skin: #e8c6b3;
    --white: #ffffff;
  }
  html, body {
    margin: 0;
    padding: 0;
    width: 848px;
    height: 1200px;
    overflow: hidden;
    background: var(--paper);
  }
  .cover {
    position: relative;
    width: 848px;
    height: 1200px;
    overflow: hidden;
    background: radial-gradient(ellipse at 50% 30%, #ffffff 0%, var(--paper) 60%, #eff0f2 100%);
    font-family: "Fredoka", "Arial Rounded MT Bold", sans-serif;
  }
  .cover-photo {
    position: absolute;
    left: 0;
    top: 540px;
    width: 848px;
    height: 660px;
    background:
      linear-gradient(180deg, rgba(251,251,252,1) 0%, rgba(251,251,252,0) 18%),
      linear-gradient(180deg, #efeeed 0%, #e7dcd4 35%, #d8c4b6 55%, #5a5a60 78%, var(--shirt) 100%);
  }
  .title {
    position: absolute;
    left: 0;
    top: 48px;
    width: 100%;
    margin: 0;
    text-align: center;
    font-family: "Cabin Sketch", "Comic Sans MS", cursive;
    font-weight: 700;
    line-height: 1;
  }
  .title-line {
    display: block;
  }
  .title-line--top {
    font-size: 112px;
    color: var(--blue);
    letter-spacing: 2px;
  }
  .title-line--bottom {
    margin-top: 14px;
    font-size: 172px;
    letter-spacing: 4px;
  }
  .c-red { color: var(--red); }
  .c-green { color: var(--green); }
  .c-blue { color: var(--blue); }
  .c-pink { color: var(--pink); }
  .c-cyan { color: var(--cyan); }
  .subtitle {
    position: absolute;
    left: 0;
    top: 352px;
    width: 100%;
    margin: 0;
    text-align: center;
    color: var(--blue);
    font-size: 24px;
    line-height: 40px;
    letter-spacing: 1.2px;
  }
  .author {
    position: absolute;
    left: 0;
    bottom: 38px;
    width: 100%;
    margin: 0;
    text-align: center;
    color: var(--white);
    font-size: 31px;
    letter-spacing: 2px;
  }
</style>
</head>
<body>
  <main class="cover">
    <div class="cover-photo" role="img" aria-label="Foto: Person in dunklem Shirt hält ein weißes Blatt mit gezeichnetem lächelndem Smiley vor ihr Gesicht"></div>

    <h1 class="title">
      <span class="title-line title-line--top">SPÄTER</span>
      <span class="title-line title-line--bottom"><span class="c-red">F</span><span class="c-green">R</span><span class="c-blue">E</span><span class="c-pink">I</span><span class="c-cyan">!</span></span>
    </h1>

    <p class="subtitle">Wie du Depressionen, Süchte und Einsamkeit<br>überwindest und dein Leben veränderst</p>

    <p class="author">Olaf Brenner</p>
  </main>
</body>
</html>
```